CD cover "Marisol Quintero"

Here I send the pictures for the cover, leaving creative freedom to the photography and any modifications you make. The artist is called Marisol Quintero, and the title of the album is called. "Over Quiet Rivers" but please translate that to Spanish. Thank you for your valuable work.
The name of the artist is: Marisol Quintero
Album Name: “Sobre ríos quietos” in Spanish

```html
<!DOCTYPE html>
<html lang="es">
<head>
<meta charset="utf-8">
<title>Sobre ríos quietos — Marisol Quintero</title>
<link href="https://fonts.googleapis.com/css2?family=Allura&family=Cormorant+SC:wght@500&display=swap" rel="stylesheet">
<style>
  :root {
    --backdrop: #dea552;
    --paper: #f0f0f0;
    --disc-paper: #f7f7f7;
    --ink: #1b1b1b;
    --mist: rgba(240, 240, 240, 0);
    --lavender: #8e80a8;
    --lavender-deep: #6f5f86;
    --sand: #d8cbb0;
    --hub-gold: #b98a3e;
    --hub-ring: #e8aa4c;
    --hub-core: #9c7236;
  }
  * { margin: 0; padding: 0; box-sizing: border-box; }
  html, body { width: 1200px; height: 900px; overflow: hidden; }
  body {
    background: var(--backdrop);
    position: relative;
    font-family: "Cormorant SC", Georgia, serif;
    color: var(--ink);
  }
  .album-title {
    font-family: "Allura", cursive;
    font-weight: 400;
    line-height: 1;
    white-space: nowrap;
  }
  .artist-name {
    font-weight: 500;
    white-space: nowrap;
  }

  /* Front cover */
  .album-cover {
    position: absolute;
    left: 188px; top: 214px;
    width: 452px; height: 452px;
    background: var(--paper);
    overflow: hidden;
  }
  .cover-photo {
    position: absolute;
    left: 0; top: 150px;
    width: 452px; height: 302px;
    background:
      linear-gradient(180deg, var(--mist) 0%, var(--lavender) 30%, var(--sand) 62%, var(--lavender-deep) 100%);
  }
  .cover-title-block {
    position: absolute;
    left: 0; right: 0; top: 100px;
    text-align: center;
  }
  .cover-title-block .album-title { font-size: 38px; }
  .cover-title-block .artist-name {
    font-size: 12px;
    letter-spacing: 0.42em;
    margin-top: 6px;
  }

  /* Disc */
  .disc {
    position: absolute;
    left: 584px; top: 232px;
    width: 436px; height: 436px;
    border-radius: 50%;
    background: var(--hub-gold);
    overflow: hidden;
  }
  .disc-face {
    position: absolute;
    left: 5px; top: 5px;
    width: 426px; height: 426px;
    border-radius: 50%;
    background: var(--disc-paper);
    overflow: hidden;
  }
  .disc-photo {
    position: absolute;
    left: 0; top: 140px;
    width: 426px; height: 286px;
    background:
      linear-gradient(180deg, var(--mist) 0%, var(--lavender) 30%, var(--sand) 62%, var(--lavender-deep) 100%);
  }
  .disc-title-block {
    position: absolute;
    left: 0; right: 0; top: 60px;
    text-align: center;
  }
  .disc-title-block .album-title { font-size: 40px; }
  .disc-title-block .artist-name {
    font-size: 12px;
    letter-spacing: 0.42em;
    margin-top: 6px;
  }
  .disc-hub {
    position: absolute;
    left: 134px; top: 134px;
    width: 168px; height: 168px;
    border-radius: 50%;
    background: var(--hub-gold);
  }
  .disc-hub-ring {
    position: absolute;
    left: 10px; top: 10px;
    width: 148px; height: 148px;
    border-radius: 50%;
    border: 3px solid var(--hub-ring);
  }
  .disc-hub-core {
    position: absolute;
    left: 50px; top: 50px;
    width: 68px; height: 68px;
    border-radius: 50%;
    background: var(--hub-core);
  }
</style>
</head>
<body>
  <section class="album-cover">
    <div class="cover-photo" role="img" aria-label="Painted landscape photo: a woman in a long blue dress walking away along a sandy path between lavender fields, with a rocky hill on the right"></div>
    <div class="cover-title-block">
      <h1 class="album-title">Sobre ríos quietos</h1>
      <p class="artist-name">Marisol Quintero</p>
    </div>
  </section>

  <section class="disc">
    <div class="disc-face">
      <div class="disc-photo" role="img" aria-label="Disc label photo: the same lavender fields and sandy path landscape"></div>
      <div class="disc-title-block">
        <h2 class="album-title">Sobre ríos quietos</h2>
        <p class="artist-name">Marisol Quintero</p>
      </div>
    </div>
    <div class="disc-hub">
      <div class="disc-hub-ring"></div>
      <div class="disc-hub-core"></div>
    </div>
  </section>
</body>
</html>
```